SEHLAN REAL ESTATE
شركة السهلان العقارية
Creative Brief
Simple
FAISAL ALQUDRANI
Real Estate Consultant & Developer
SAUDI ARABIA.JEDDAH
f_alqudrani@mailvesta.com
THE LOGO
Yasahiro17 Yasahiro17
YADESIGN YADESIGN

```html
<!DOCTYPE html>
<html lang="en">
<head>
<meta charset="utf-8">
<title>Sehlan Real Estate – Business Card</title>
<link href="https://fonts.googleapis.com/css2?family=Montserrat:wght@400;600;700&family=Cairo:wght@600&display=swap" rel="stylesheet">
<style>
  :root {
    --bg: #e4e5e7;
    --paper: #ffffff;
    --blue: #1d7bc1;
    --blue-dark: #15609b;
    --slate: #3d4450;
    --slate-deep: #2b3039;
    --ink: #4a4f57;
    --muted: #7a7f87;
  }
  * { margin: 0; padding: 0; box-sizing: border-box; }
  html, body { width: 1200px; height: 802px; overflow: hidden; }
  body {
    background: var(--bg);
    font-family: "Montserrat", Arial, sans-serif;
    position: relative;
  }
  .card {
    position: absolute;
    top: 246px;
    width: 540px;
    height: 310px;
    overflow: hidden;
    box-shadow: 0 6px 18px rgba(0,0,0,.18);
  }
  .card-front { left: 45px; background: var(--paper); }
  .card-back  { left: 615px; }

  .front-shapes { position: absolute; inset: 0; }

  .brand {
    position: absolute;
    left: 34px; top: 108px;
    width: 170px;
    text-align: center;
  }
  .brand-name {
    display: flex; align-items: center; justify-content: center; gap: 8px;
    font-weight: 700; font-size: 22px; color: var(--blue-dark); letter-spacing: 1px;
  }
  .brand-mark { width: 14px; height: 14px; background: var(--blue); }
  .brand-sub { font-size: 8px; letter-spacing: 2.4px; color: var(--slate); margin-top: 4px; font-weight: 600; }
  .brand-arabic { font-family: "Cairo", sans-serif; font-size: 13px; color: var(--slate); margin-top: 4px; }

  .divider {
    position: absolute; left: 222px; top: 78px;
    width: 1.5px; height: 128px; background: var(--blue);
  }
  .contact { position: absolute; left: 240px; top: 78px; }
  .person-name { font-size: 17px; font-weight: 700; color: var(--blue); letter-spacing: .5px; }
  .person-title { font-size: 9.5px; color: var(--muted); margin-top: 3px; }
  .contact-list { list-style: none; margin-top: 16px; }
  .contact-list li {
    display: flex; align-items: center; gap: 8px;
    font-size: 10px; color: var(--ink); margin-bottom: 8px;
  }
  .contact-icon { width: 14px; height: 14px; flex: none; }

  .location {
    position: absolute; right: 24px; bottom: 12px;
    font-size: 10.5px; font-weight: 600; letter-spacing: 1px; color: #fff;
  }

  .back-fill {
    position: absolute; inset: 0;
    background: linear-gradient(135deg, #4a5260 0%, var(--slate) 45%, var(--slate-deep) 100%);
  }
  .back-brand {
    position: absolute; left: 0; right: 0; top: 50%;
    transform: translateY(-50%);
    display: flex; align-items: center; justify-content: center; gap: 10px;
    font-weight: 700; font-size: 28px; letter-spacing: 2px; color: var(--blue);
  }
  .back-brand .brand-mark { width: 18px; height: 18px; }
</style>
</head>
<body>

<section class="card card-front" aria-label="Business card front">
  <svg class="front-shapes" viewBox="0 0 540 310" width="540" height="310" aria-hidden="true">
    <!-- roof band, top right -->
    <polygon points="250,40 470,40 495,14 520,40 540,40 540,52 520,52 495,28 470,52 262,52" fill="#3d4450"/>
    <polygon points="262,52 470,52 495,28 520,52 540,52 540,58 520,58 495,34 470,58 268,58" fill="#1d7bc1"/>
    <!-- bottom bands -->
    <polygon points="0,262 540,262 540,272 0,272" fill="#1d7bc1"/>
    <polygon points="170,272 540,272 540,310 140,310" fill="#3d4450"/>
    <polygon points="0,272 170,272 140,310 0,310" fill="#1d7bc1"/>
  </svg>

  <div class="brand">
    <div class="brand-name"><span class="brand-mark"></span>SEHLAN</div>
    <div class="brand-sub">REAL ESTATE</div>
    <div class="brand-arabic" lang="ar" dir="rtl">شركة السهلان العقارية</div>
  </div>

  <div class="divider"></div>

  <div class="contact">
    <div class="person-name">FAISAL ALQUDRANI</div>
    <div class="person-title">Real Estate Consultant &amp; Developer</div>
    <ul class="contact-list">
      <li>
        <svg class="contact-icon" viewBox="0 0 14 14"><circle cx="7" cy="7" r="7" fill="#1d7bc1"/><path d="M4.6 3.6l1.3 1.4-.7.9c.5 1 1.3 1.8 2.3 2.3l.9-.7 1.4 1.3-.8 1c-2.5-.3-4.9-2.7-5.2-5.2z" fill="#fff"/></svg>
        +966555014272
      </li>
      <li>
        <svg class="contact-icon" viewBox="0 0 14 14"><circle cx="7" cy="7" r="7" fill="#1d7bc1"/><rect x="3.5" y="4.5" width="7" height="5" fill="none" stroke="#fff" stroke-width="1"/><path d="M3.5 4.5L7 7.3l3.5-2.8" fill="none" stroke="#fff" stroke-width="1"/></svg>
        f_alqudrani@mailvesta.com
      </li>
      <li>
        <svg class="contact-icon" viewBox="0 0 14 14"><circle cx="7" cy="7" r="7" fill="#1d7bc1"/><circle cx="7" cy="7" r="3.6" fill="none" stroke="#fff" stroke-width="1"/><path d="M3.4 7h7.2M7 3.4c-1.6 2-1.6 5.2 0 7.2M7 3.4c1.6 2 1.6 5.2 0 7.2" fill="none" stroke="#fff" stroke-width=".8"/></svg>
        www.sehlanestate.com
      </li>
    </ul>
  </div>

  <div class="location">SAUDI ARABIA.JEDDAH</div>
</section>

<section class="card card-back" aria-label="Business card back">
  <div class="back-fill" role="img" aria-label="Dark slate background with a repeating embossed brand pattern"></div>
  <div class="back-brand"><span class="brand-mark"></span>SEHLAN</div>
</section>

</body>
</html>
```